Refresh of Business Card Design

Want to refresh the business card design with the new logo while adhering to style guide as attached. Would like to match feel of website www.durmackvinex.com

```html
<!DOCTYPE html>
<html lang="en">
<head>
<meta charset="utf-8">
<title>Durmack Vinex – Business Card</title>
<link href="https://fonts.googleapis.com/css2?family=Open+Sans:wght@400;600;700;800&display=swap" rel="stylesheet">
<style>
  :root {
    --backdrop: #3b3b3b;
    --card: #161616;
    --card-edge: #d8232a;
    --accent: #e0262d;
    --text: #f1f1f1;
    --muted: #bdbdbd;
    --mark-dim: #6a6a6a;
  }
  * { box-sizing: border-box; margin: 0; padding: 0; }
  html, body { width: 1200px; height: 801px; overflow: hidden; }
  body {
    background: var(--backdrop);
    font-family: "Open Sans", Arial, sans-serif;
    position: relative;
  }
  .card {
    position: absolute;
    top: 252px;
    width: 520px;
    height: 297px;
    background: var(--card);
    border-bottom: 3px solid var(--card-edge);
    box-shadow: 0 10px 30px rgba(0,0,0,.45);
  }
  .card--front { left: 45px; }
  .card--back { left: 635px; }

  /* wordmark */
  .wordmark { display: flex; align-items: center; gap: 10px; }
  .wordmark__dot { width: 16px; height: 16px; border-radius: 50%; background: var(--accent); flex: none; }
  .wordmark__name { font-weight: 700; color: var(--text); letter-spacing: 1px; text-transform: uppercase; }
  .card--front .wordmark { position: absolute; left: 36px; top: 116px; }
  .card--front .wordmark__name { font-size: 19px; }

  .card--back .wordmark { position: absolute; left: 0; right: 0; top: 128px; justify-content: center; }
  .card--back .wordmark__dot { background: var(--mark-dim); width: 22px; height: 22px; }
  .card--back .wordmark__name { color: var(--mark-dim); font-size: 28px; letter-spacing: 2px; }

  /* person */
  .person { position: absolute; right: 32px; top: 28px; text-align: right; }
  .person__name { color: var(--accent); font-weight: 800; font-size: 19px; letter-spacing: .3px; }
  .person__role { color: var(--muted); font-size: 12px; margin-top: -2px; }

  .rule { position: absolute; height: 1px; background: var(--accent); }
  .rule--top { right: 32px; top: 84px; width: 230px; }
  .rule--bottom { left: 32px; right: 32px; top: 214px; }

  .address { position: absolute; right: 32px; top: 118px; text-align: right; color: var(--text); font-size: 13px; line-height: 1.6; }

  .contacts { position: absolute; left: 32px; top: 226px; list-style: none; color: var(--text); font-size: 13px; line-height: 1.45; }
  .contacts li { display: flex; align-items: center; gap: 8px; }
  .contacts svg { width: 11px; height: 11px; fill: var(--accent); flex: none; }
</style>
</head>
<body>
  <section class="card card--front" aria-label="Card front">
    <div class="wordmark">
      <span class="wordmark__dot"></span>
      <span class="wordmark__name">Durmack Vinex</span>
    </div>

    <div class="person">
      <p class="person__name">REID CALLOWAY</p>
      <p class="person__role">Sales</p>
    </div>
    <div class="rule rule--top"></div>

    <p class="address">
      P.O. Box 40213 Lindale, TX 7940<br>
      212 Harlow Dr Kessler, Texas 79002
    </p>

    <div class="rule rule--bottom"></div>

    <ul class="contacts">
      <li>
        <svg viewBox="0 0 24 24" aria-hidden="true"><path d="M6.6 10.8a15 15 0 0 0 6.6 6.6l2.2-2.2c.3-.3.7-.4 1-.2 1.1.4 2.3.6 3.6.6.6 0 1 .4 1 1V20c0 .6-.4 1-1 1A17 17 0 0 1 3 4c0-.6.4-1 1-1h3.5c.6 0 1 .4 1 1 0 1.3.2 2.5.6 3.6.1.3 0 .7-.2 1z"/></svg>
        555.201.4378
      </li>
      <li>
        <svg viewBox="0 0 24 24" aria-hidden="true"><path d="M2 5h20v14H2zm2 2v.5l8 5 8-5V7l-8 5z"/></svg>
        rcalloway@durmackvinex.com
      </li>
      <li>
        <svg viewBox="0 0 24 24" aria-hidden="true"><path d="M12 2a10 10 0 1 0 0 20 10 10 0 0 0 0-20zm6.9 6h-3a15 15 0 0 0-1.3-3.9A8 8 0 0 1 18.9 8zM12 4a13 13 0 0 1 1.9 4h-3.8A13 13 0 0 1 12 4zM4.3 14a8 8 0 0 1 0-4h3.4a16 16 0 0 0 0 4zm.8 2h3a15 15 0 0 0 1.3 3.9A8 8 0 0 1 5.1 16zm3-8h-3a8 8 0 0 1 4.3-3.9A15 15 0 0 0 8.1 8zM12 20a13 13 0 0 1-1.9-4h3.8A13 13 0 0 1 12 20zm2.3-6H9.7a14 14 0 0 1 0-4h4.6a14 14 0 0 1 0 4zm.3 5.9a15 15 0 0 0 1.3-3.9h3a8 8 0 0 1-4.3 3.9zm1.7-5.9a16 16 0 0 0 0-4h3.4a8 8 0 0 1 0 4z"/></svg>
        www.durmackvinex.com
      </li>
    </ul>
  </section>

  <section class="card card--back" aria-label="Card back">
    <div class="wordmark">
      <span class="wordmark__dot"></span>
      <span class="wordmark__name">Durmack Vinex</span>
    </div>
  </section>
</body>
</html>
```